Australian Wine export company Need a Wine label design

We need a wine label design for a new branded Australian wine based in South Australia called " HALLORAN " .
We will use this brand name ' HALLORAN' to marketing Australian Red wine and White wine into Chinese Market.
We would like to see the label designs that look classic and make consumers feel this is a superior quality Australian wine.
This label is to promote AUSTRALIAN WINE, need wine related and country related theme, need to give the consumer first impression that this wine is from AUSTRALIA.

Thanks
Updates

The following information are required to be presented on the wine label:

1) Brand Name: Halloran
2) Logo
3) Year of Vintage
4) Varietal
5) Place of production: South Australia
6) Fine Wine of Australia

Thanks.

Target Market(s)

Chinese market

Industry/Entity Type

Marketing

Requirements
Must have
• Need label design and renderings on the bottles.
Nice to have
• Label make consumers feel this is a superior quality Australian Wine.

```html
<!DOCTYPE html>
<html lang="en">
<head>
<meta charset="utf-8">
<title>Halloran – Australian Wine Label</title>
<link rel="stylesheet" href="https://fonts.googleapis.com/css2?family=Tinos:ital,wght@0,400;1,400&display=swap">
<style>
  :root {
    --paper: #ffffff;
    --ink: #000000;
    --royal: #2c3a9c;
    --cream: #d9d09b;
    --gold: #e3d79a;
    --white: #ffffff;
    --label-font: "Tinos", "Times New Roman", serif;
  }
  html, body {
    margin: 0;
    padding: 0;
    overflow: hidden;
  }
  body {
    width: 1200px;
    height: 927px;
    background: var(--paper);
    position: relative;
    font-family: var(--label-font);
  }
  .neck-label {
    position: absolute;
    left: 428px;
    top: 60px;
    width: 344px;
    height: 217px;
    background: var(--ink);
    border-top: 22px solid var(--royal);
    border-bottom: 22px solid var(--royal);
    box-sizing: border-box;
  }
  .front-label {
    position: absolute;
    left: 438px;
    top: 327px;
    width: 324px;
    height: 488px;
    display: block;
  }
  .front-label text {
    font-family: var(--label-font);
  }
</style>
</head>
<body>
  <div class="neck-label" aria-label="Neck label"></div>

  <svg class="front-label" viewBox="0 0 324 488" aria-label="Halloran front label">
    <defs>
      <radialGradient id="burst" cx="50%" cy="40%" r="60%">
        <stop offset="0" stop-color="#5a5a5a"/>
        <stop offset="0.55" stop-color="#1a1a1a"/>
        <stop offset="1" stop-color="#000"/>
      </radialGradient>
      <linearGradient id="footer-shine" x1="0" y1="0" x2="0" y2="1">
        <stop offset="0" stop-color="#000"/>
        <stop offset="0.45" stop-color="#3a3a3a"/>
        <stop offset="1" stop-color="#000"/>
      </linearGradient>
      <radialGradient id="vine-tone" cx="50%" cy="45%" r="55%">
        <stop offset="0" stop-color="#e8e8e8"/>
        <stop offset="1" stop-color="#9a9a9a"/>
      </radialGradient>
    </defs>

    <!-- label ground -->
    <rect class="label-ground" x="1.5" y="1.5" width="321" height="485" fill="var(--cream)" stroke="var(--royal)" stroke-width="3"/>

    <!-- cartouche -->
    <path class="cartouche" fill="url(#burst)" stroke="var(--royal)" stroke-width="4"
      d="M18,80 Q38,78 44,56 Q80,50 120,40 Q162,6 204,40 Q244,50 280,56 Q286,78 306,80 L306,300 Q286,302 280,326 Q240,334 200,352 Q162,370 124,352 Q84,334 44,326 Q38,302 18,300 Z"/>
    <path class="cartouche-keyline" fill="none" stroke="var(--white)" stroke-width="1"
      transform="translate(162 205) scale(0.94) translate(-162 -205)"
      d="M18,80 Q38,78 44,56 Q80,50 120,40 Q162,6 204,40 Q244,50 280,56 Q286,78 306,80 L306,300 Q286,302 280,326 Q240,334 200,352 Q162,370 124,352 Q84,334 44,326 Q38,302 18,300 Z"/>

    <g class="vine-illustration" role="img" aria-label="Grape cluster with vine leaf illustration">
      <ellipse cx="158" cy="92" rx="44" ry="30" fill="url(#vine-tone)" opacity="0.9"/>
    </g>

    <text class="brand-name" x="162" y="201" text-anchor="middle" font-size="33" fill="var(--white)" letter-spacing="1">HALLORAN</text>
    <line class="brand-rule" x1="72" y1="213" x2="252" y2="213" stroke="var(--white)" stroke-width="1.5"/>
    <text class="brand-tagline" x="162" y="228" text-anchor="middle" font-size="10" font-style="italic" fill="var(--white)">Australian Wine</text>

    <text class="vintage-caption" x="162" y="298" text-anchor="middle" font-size="11" font-style="italic" fill="var(--white)">Vintage</text>
    <text class="vintage-year" x="162" y="322" text-anchor="middle" font-size="23" font-style="italic" fill="var(--white)" letter-spacing="2">2000</text>

    <!-- varietal band -->
    <rect class="varietal-band" x="6" y="372" width="312" height="30" fill="var(--ink)"/>
    <line x1="6" y1="375" x2="318" y2="375" stroke="var(--white)" stroke-width="1"/>
    <line x1="6" y1="399" x2="318" y2="399" stroke="var(--white)" stroke-width="1"/>
    <text class="varietal" x="162" y="393" text-anchor="middle" font-size="15" fill="var(--white)" letter-spacing="2.5">VARIETAL</text>

    <!-- details panel -->
    <rect class="details-panel" x="6" y="406" width="312" height="74" fill="url(#footer-shine)"/>
    <text class="volume" x="162" y="424" text-anchor="middle" font-size="12" fill="var(--white)">750ml</text>
    <text class="alcohol" x="162" y="438" text-anchor="middle" font-size="10" fill="var(--white)">14% alc/vol</text>
    <text class="origin-caption" x="162" y="452" text-anchor="middle" font-size="10" fill="var(--white)">Place of Production</text>
    <text class="origin" x="162" y="471" text-anchor="middle" font-size="17" fill="var(--gold)">South Australia</text>
  </svg>
</body>
</html>
```